Gift Card Design - Suds Harbor Co

I am needing a design for a standard plastic gift card, (ever so slightly large then a standard rounded edge business card). Name of the business is Suds Harbor Co. Attached is a file with a poor example, done by an equipment manufacturing firm, that I feel could be much better. Simple, clean and classy with what it is and does along with our name is what I am looking for. Attached also is out logo and source of logo, they don't have to be on the card.

Target Market(s)

Car wash customers in an upscale market.

Industry/Entity Type

Business

Font styles to use
Serif
Other font styles liked:
• whatever you feel, but I do like the font on a Brevanto golf ball

Requirements
Must have
• Words anywhere on the card -
• Reloadable Card
• Self Serve Bays & Vacuums.
• Also need name of the business, Suds Harbor Co.
Nice to have
• Work in Pantone #7483 as there is existing signage with that as a primary color, just trying to tie things together. Attached is my business logo and a picture of the source of the logo, you do not have to use those if you don't want to. I do like clean and classy but am open to creativity, that's why I am submitting this project.
Should not have
• Naked lady pictures

```html
<!DOCTYPE html>
<html lang="en">
<head>
<meta charset="utf-8">
<title>Suds Harbor Co – Reloadable Card</title>
<link rel="stylesheet" href="https://fonts.googleapis.com/css2?family=Yesteryear&family=Cormorant+Garamond:wght@500&family=Arimo&display=swap">
<style>
  :root {
    --page: #ffffff;
    --card-top: #22808c;
    --card-bottom: #1a6e7b;
    --ink-light: #e4f6f7;
    --accent: #4fd0ea;
  }
  * { margin: 0; padding: 0; box-sizing: border-box; }
  html, body {
    width: 1200px;
    height: 782px;
    overflow: hidden;
    background: var(--page);
  }
  .card {
    position: absolute;
    left: 30px;
    top: 39px;
    width: 1140px;
    height: 704px;
    border-radius: 14px;
    background: linear-gradient(180deg, var(--card-top), var(--card-bottom));
    overflow: hidden;
  }
  .corner-stripes {
    position: absolute;
    right: 0;
    top: 0;
    width: 140px;
    height: 120px;
  }
  .brand-title {
    position: absolute;
    left: 0;
    width: 100%;
    top: 40px;
    text-align: center;
    font-family: "Yesteryear", cursive;
    font-size: 108px;
    line-height: 1;
    color: var(--ink-light);
    letter-spacing: 4px;
  }
  .card-type {
    position: absolute;
    left: 312px;
    top: 172px;
    width: 518px;
    height: 84px;
    border-top: 2px solid var(--accent);
    border-bottom: 2px solid var(--accent);
    display: flex;
    align-items: center;
    justify-content: center;
    font-family: "Cormorant Garamond", serif;
    font-weight: 500;
    font-size: 66px;
    letter-spacing: 3px;
    color: var(--ink-light);
  }
  .services {
    position: absolute;
    left: 590px;
    top: 470px;
    width: 500px;
    text-align: center;
    font-family: "Arimo", sans-serif;
    font-size: 54px;
    line-height: 84px;
    letter-spacing: 5px;
    color: var(--ink-light);
  }
  .brand-mark {
    position: absolute;
    left: 40px;
    top: 520px;
    width: 460px;
    text-align: center;
    font-family: "Cormorant Garamond", serif;
    font-weight: 500;
    font-size: 52px;
    letter-spacing: 3px;
    color: var(--accent);
  }
</style>
</head>
<body>
  <main class="card">
    <svg class="corner-stripes" viewBox="0 0 140 120" aria-hidden="true">
      <line x1="0" y1="0" x2="140" y2="120" stroke="#4fd0ea" stroke-width="9"/>
      <line x1="52" y1="0" x2="140" y2="76" stroke="#4fd0ea" stroke-width="9"/>
    </svg>

    <h1 class="brand-title">Suds Harbor Co</h1>
    <p class="card-type">Reloadable Card</p>

    <p class="services">Self Serve<br>Bays &amp; Vacuums</p>

    <p class="brand-mark">Suds Harbor Co</p>
  </main>
</body>
</html>
```